Business Card Design

I need a business card design. I am a sole practitioner.I am a psychotherapist and I need a professional card. I am also an art therapist (a form of psychotherapy using art) so I want the image to be professional/creative/maybe ethnic. I do not want a boring minimalist "medical" image, nor do I want it too hippy/tree hugging.
Colours like reds/ochres/yellows would be good.
Industry/Entity Type
Business
Contact Information for Business Card
Mira Tanvel
Psychotherapy, Counselling and Art Therapy
Korrabel Lodge Counselling and Wellbeing services
17 Farrow Lane, Pelbury 4091
0419362750 www.MiraTanvel.com.au
on rear of card I need the option to have at least 4 or 5 appointment times /dates
Look and feel
Each slider illustrates characteristics of the customer's brand and the style your logo design should communicate.

```html
<!DOCTYPE html>
<html lang="en">
<head>
<meta charset="utf-8">
<title>Mira Tanvel – Business Card</title>
<link rel="stylesheet" href="https://fonts.googleapis.com/css2?family=Alegreya+SC:wght@500&family=Alegreya:wght@400&family=Open+Sans:wght@400;700&display=swap">
<style>
  :root {
    --backdrop: #1c1c1e;
    --paper: #ffffff;
    --ink: #1d1b19;
    --ink-soft: #3a3632;
    --gold-dark: #8a6a32;
    --gold: #b8934f;
    --gold-light: #e6cf9c;
  }
  * { box-sizing: border-box; margin: 0; padding: 0; }
  html, body { width: 1200px; height: 900px; overflow: hidden; }
  body {
    background: var(--backdrop);
    display: flex;
    flex-direction: column;
    align-items: center;
    justify-content: center;
    gap: 56px;
    font-family: "Open Sans", sans-serif;
    color: var(--ink);
  }
  .card {
    position: relative;
    width: 660px;
    height: 377px;
    background: var(--paper);
    overflow: hidden;
    box-shadow: 0 10px 30px rgba(0,0,0,.45);
  }
  .gold-band {
    position: absolute;
    top: 0; bottom: 0;
    background: linear-gradient(160deg, var(--gold-dark) 0%, var(--gold) 35%, var(--gold-light) 60%, var(--gold) 85%, var(--gold-dark) 100%);
  }
  .card--front .gold-band { right: 0; width: 152px; }
  .card--back .gold-band--left { left: 0; width: 26px; }
  .card--back .gold-band--right { right: 0; width: 190px; }

  /* Front */
  .brand {
    position: absolute;
    left: 38px; top: 40px;
    display: flex;
    align-items: center;
    gap: 20px;
  }
  .brand__mark {
    width: 104px; height: 104px;
    background: var(--gold);
  }
  .brand__name {
    font-family: "Alegreya SC", serif;
    font-weight: 500;
    font-size: 50px;
    line-height: 1;
    color: var(--ink);
    letter-spacing: 1px;
  }
  .brand__tagline {
    font-family: "Alegreya", serif;
    font-size: 17px;
    color: var(--ink);
    margin-top: 8px;
    margin-left: 4px;
  }
  .practice {
    position: absolute;
    left: 38px; top: 176px;
    padding-left: 8px;
    border-left: 2px solid var(--gold);
    font-family: "Alegreya", serif;
    font-size: 18px;
    line-height: 1.2;
    color: var(--ink);
  }
  .contact {
    position: absolute;
    left: 36px; top: 246px;
    list-style: none;
    font-size: 14px;
    line-height: 24px;
    color: var(--ink-soft);
    font-weight: 700;
  }
  .contact li { display: flex; align-items: center; gap: 8px; }
  .contact svg { width: 16px; height: 16px; fill: var(--gold-dark); flex: none; }

  /* Back */
  .back-brand {
    position: absolute;
    left: 58px; top: 28px;
    display: flex;
    flex-direction: column;
    align-items: center;
    gap: 4px;
  }
  .back-brand__mark { width: 64px; height: 64px; background: var(--gold); }
  .back-brand__name {
    font-family: "Alegreya SC", serif;
    font-weight: 500;
    font-size: 13px;
    color: var(--ink);
  }
  .appointments {
    position: absolute;
    left: 50px; top: 130px;
  }
  .appointments__title {
    font-weight: 700;
    font-size: 17px;
    padding-left: 6px;
    border-left: 2px solid var(--gold);
    margin-bottom: 6px;
  }
  .appointments__list { list-style: none; }
  .appointments__row {
    display: flex;
    align-items: center;
    gap: 8px;
    font-size: 15px;
    line-height: 29px;
    color: var(--ink-soft);
  }
  .appointments__num { width: 16px; font-weight: 700; }
  .appointments__icon {
    width: 26px; height: 17px;
    background: var(--gold-dark);
    border-radius: 2px;
  }
  .appointments__blank {
    display: inline-block;
    border-bottom: 1px solid var(--ink-soft);
    height: 16px;
  }
  .appointments__blank--s { width: 40px; }
  .appointments__blank--l { width: 58px; }
  .appointments__time { display: flex; align-items: center; gap: 8px; margin-left: 22px; }
</style>
</head>
<body>

  <section class="card card--front" aria-label="Business card front">
    <div class="brand">
      <div class="brand__mark"></div>
      <div>
        <div class="brand__name">Mira Tanvel</div>
        <div class="brand__tagline">Psychotherapy and Counselling</div>
      </div>
    </div>
    <p class="practice">Korrabel Lodge Counselling &amp;<br>Wellbeing Services</p>
    <ul class="contact">
      <li><svg viewBox="0 0 16 16"><path d="M8 1a5 5 0 0 0-5 5c0 3.5 5 9 5 9s5-5.5 5-9a5 5 0 0 0-5-5zm0 7a2 2 0 1 1 0-4 2 2 0 0 1 0 4z"/></svg>17 Farrow Lane, Pelbury, 4091</li>
      <li><svg viewBox="0 0 16 16"><path d="M4 1l3 3-2 2a9 9 0 0 0 5 5l2-2 3 3-2 3C7 15 1 9 1 3z"/></svg>0419-362-750</li>
      <li><svg viewBox="0 0 16 16"><path d="M1 3h14v10H1zm1 1v1l6 4 6-4V4z"/></svg>Email.</li>
      <li><svg viewBox="0 0 16 16"><path d="M1 2h14v9H1zm5 10h4v1h2v1H4v-1h2z"/></svg>www.MiraTanvel.com.au</li>
    </ul>
    <div class="gold-band" role="img" aria-label="Gold decorative pattern band"></div>
  </section>

  <section class="card card--back" aria-label="Business card back">
    <div class="gold-band gold-band--left" role="img" aria-label="Gold decorative pattern strip"></div>
    <div class="back-brand">
      <div class="back-brand__mark"></div>
      <div class="back-brand__name">Mira Tanvel</div>
    </div>
    <div class="appointments">
      <h2 class="appointments__title">Appointment</h2>
      <ol class="appointments__list">
        <li class="appointments__row"><span class="appointments__num">1·</span><span class="appointments__icon"></span>DATE: <span class="appointments__blank appointments__blank--s"></span>/<span class="appointments__blank appointments__blank--s"></span>/<span class="appointments__blank appointments__blank--l"></span><span class="appointments__time"><span class="appointments__icon"></span><span class="appointments__blank appointments__blank--l"></span></span></li>
        <li class="appointments__row"><span class="appointments__num">2·</span><span class="appointments__icon"></span>DATE: <span class="appointments__blank appointments__blank--s"></span>/<span class="appointments__blank appointments__blank--s"></span>/<span class="appointments__blank appointments__blank--l"></span><span class="appointments__time"><span class="appointments__icon"></span><span class="appointments__blank appointments__blank--l"></span></span></li>
        <li class="appointments__row"><span class="appointments__num">3·</span><span class="appointments__icon"></span>DATE: <span class="appointments__blank appointments__blank--s"></span>/<span class="appointments__blank appointments__blank--s"></span>/<span class="appointments__blank appointments__blank--l"></span><span class="appointments__time"><span class="appointments__icon"></span><span class="appointments__blank appointments__blank--l"></span></span></li>
        <li class="appointments__row"><span class="appointments__num">4·</span><span class="appointments__icon"></span>DATE: <span class="appointments__blank appointments__blank--s"></span>/<span class="appointments__blank appointments__blank--s"></span>/<span class="appointments__blank appointments__blank--l"></span><span class="appointments__time"><span class="appointments__icon"></span><span class="appointments__blank appointments__blank--l"></span></span></li>
        <li class="appointments__row"><span class="appointments__num">5·</span><span class="appointments__icon"></span>DATE: <span class="appointments__blank appointments__blank--s"></span>/<span class="appointments__blank appointments__blank--s"></span>/<span class="appointments__blank appointments__blank--l"></span><span class="appointments__time"><span class="appointments__icon"></span><span class="appointments__blank appointments__blank--l"></span></span></li>
      </ol>
    </div>
    <div class="gold-band gold-band--right" role="img" aria-label="Gold decorative pattern band"></div>
  </section>

</body>
</html>
```